4"x9" Roofing Flyer Design - Tile Roofing!

We are looking to create a 4"x9" double sided flyer in full color that displays pictures of before and after of tile underlayment replacement. This would have words as well.

The theme should match the overall theme of our brochure that we already have designed so they are cohesive.

I have uploaded an example of a similar flyer that we like the overall layout of.

Please read the "Design Wording" PDF I uploaded for the words and overall design layout we are looking for on this brochure.

Please let me know if you'd like more photos or anything like that.

Target Market(s)

Retirees

Industry/Entity Type

Roofing

Font styles to use
Other font styles liked:
• Match existing fonts from our brochure

Requirements
Must have
• Must match style of existing brochure (uploaded), font must match closely as well

```html
<!DOCTYPE html>
<html lang="en">
<head>
<meta charset="utf-8">
<title>Juniper Ridge Roofing – Tile Underlayment Flyer</title>
<link rel="stylesheet" href="https://fonts.googleapis.com/css2?family=Arvo:wght@700&family=Montserrat:wght@500&family=Roboto:wght@400&family=Roboto+Slab:wght@300;400;500&display=swap">
<style>
  :root {
    --stage: #e4e4e4;
    --charcoal: #262626;
    --charcoal-deep: #1c1c1c;
    --orange: #ec5a1c;
    --white: #ffffff;
    --text: #e9e9e9;
  }
  * { box-sizing: border-box; margin: 0; padding: 0; }
  html, body { width: 1200px; height: 3041px; overflow: hidden; background: var(--stage); }
  .flyer {
    position: absolute; top: 890px; width: 560px; height: 1260px;
    background: var(--charcoal); overflow: hidden;
    box-shadow: 0 4px 14px rgba(0,0,0,.18);
  }
  .flyer--front { left: 27px; }
  .flyer--back { left: 613px; }
  .flyer__art { position: absolute; inset: 0; width: 560px; height: 1260px; }
  .brand { position: absolute; top: 118px; left: 0; width: 100%; text-align: center; }
  .brand__name {
    display: inline-flex; align-items: center; gap: 12px;
    font-family: "Arvo", serif; font-weight: 700; font-size: 40px; color: var(--white);
  }
  .brand__mark { width: 18px; height: 18px; background: var(--orange); display: inline-block; }
  .brand__phone {
    font-family: "Montserrat", sans-serif; font-weight: 500; font-size: 53px;
    color: var(--orange); line-height: 1.25; margin-top: 6px;
  }
  .brand__tagline {
    font-family: "Roboto", sans-serif; font-size: 19px; color: var(--white); letter-spacing: .3px;
  }
  .copy {
    position: absolute; left: 52px; right: 52px;
    font-family: "Roboto Slab", serif; font-weight: 300; font-size: 14.2px;
    line-height: 1.22; color: var(--text);
  }
  .copy p { margin-bottom: 12px; }
  .copy ul { list-style: none; margin-bottom: 12px; }
  .copy li { position: relative; padding-left: 14px; margin-bottom: 12px; }
  .copy li::before { content: "•"; position: absolute; left: 0; color: var(--orange); }
  .hl { color: var(--orange); }
  .hl-strong { color: var(--orange); font-weight: 500; }
  .label { background: var(--white); color: var(--orange); font-weight: 500; padding: 0 2px; }
  .headline { position: absolute; left: 52px; top: 620px; font-family: "Roboto Slab", serif; font-weight: 500; }
  .headline__top { font-size: 26px; color: var(--orange); line-height: 1.2; }
  .headline__bottom { font-size: 24px; color: var(--white); line-height: 1.3; }
  .headline__rule { width: 140px; height: 4px; background: var(--orange); margin-top: 6px; border-radius: 2px; }
  .footer-info {
    position: absolute; right: 50px; top: 1196px; text-align: right;
    font-family: "Roboto Slab", serif; font-size: 11px; line-height: 1.3;
  }
  .footer-info__web { color: var(--white); font-weight: 500; }
  .footer-info__license { color: var(--orange); font-weight: 500; }
</style>
</head>
<body>

<section class="flyer flyer--front">
  <svg class="flyer__art" viewBox="0 0 560 1260">
    <defs>
      <linearGradient id="tileBeige" x1="0" y1="0" x2="1" y2="1">
        <stop offset="0" stop-color="#b59a82"/><stop offset="1" stop-color="#8a7260"/>
      </linearGradient>
      <linearGradient id="underlayGrey" x1="0" y1="0" x2="1" y2="1">
        <stop offset="0" stop-color="#9a9893"/><stop offset="1" stop-color="#4e4c48"/>
      </linearGradient>
      <linearGradient id="stackedTiles" x1="0" y1="0" x2="1" y2="1">
        <stop offset="0" stop-color="#8fb3dc"/><stop offset=".45" stop-color="#5d6a80"/><stop offset="1" stop-color="#2d3340"/>
      </linearGradient>
    </defs>
    <polygon points="0,250 120,340 120,362 0,274" fill="var(--orange)"/>
    <polyline points="0,290 100,366" stroke="var(--white)" stroke-width="3" fill="none"/>
    <polygon points="560,250 440,340 440,362 560,274" fill="var(--orange)"/>
    <polyline points="560,290 460,366" stroke="var(--white)" stroke-width="3" fill="none"/>
    <polygon points="0,700 0,760 14,720" fill="var(--orange)" opacity="0"/>
    <rect x="17" y="350" width="254" height="240" fill="var(--white)"/>
    <rect x="21" y="354" width="246" height="232" fill="url(#tileBeige)" role="img" aria-label="Photo of an aged concrete tile roof surface"/>
    <rect x="289" y="350" width="254" height="240" fill="var(--white)"/>
    <rect x="293" y="354" width="246" height="232" fill="url(#underlayGrey)" role="img" aria-label="Close-up photo of cracked, brittle roof underlayment beneath the tiles"/>
    <polygon points="0,1160 330,1045 560,1110 560,1260 0,1260" fill="url(#stackedTiles)" role="img" aria-label="Photo of removed tiles stacked on a roof during re-lay"/>
    <polyline points="0,1140 330,1024 560,1090" stroke="var(--orange)" stroke-width="16" fill="none"/>
    <polyline points="0,1118 330,1004 560,1070" stroke="var(--white)" stroke-width="3" fill="none"/>
  </svg>

  <header class="brand">
    <div class="brand__name"><span class="brand__mark"></span>Juniper Ridge Roofing</div>
    <div class="brand__phone">(555) 214-0377</div>
    <div class="brand__tagline">QUALITY ROOFING YOU CAN TRUST</div>
  </header>

  <div class="headline">
    <div class="headline__top">The Hidden Clock Ticking</div>
    <div class="headline__bottom">Under Your Tiles</div>
    <div class="headline__rule"></div>
  </div>

  <div class="copy" style="top:725px;">
    <p>When a tile roof is installed, the tiles themselves are not waterproof—they are simply a shield. The actual waterproofing is done by the felt or synthetic underlayment installed beneath them. In homes of your vintage, this underlayment is now:</p>
    <ul>
      <li><span class="hl">Brittle and Chalky:</span> It cracks and turns into powder under the constant heat cycles, losing its waterproofing integrity.</li>
      <li><span class="hl">Compromised:</span> Even a single leak in a neighboring home means the moisture risk has increased exponentially across the entire block.</li>
    </ul>
    <p>Based on the age and materials used in this specific neighborhood, underlayment failure is not a matter of if, but when.</p>
    <p>Waiting for a visible ceiling stain often means the damage has already spread to the roof deck, rafters, and interior walls. A slow leak can silently cost thousands in remediation before you ever see a drop.</p>
  </div>
</section>

<section class="flyer flyer--back">
  <svg class="flyer__art" viewBox="0 0 560 1260">
    <defs>
      <linearGradient id="homeAerial" x1="0" y1="0" x2="0" y2="1">
        <stop offset="0" stop-color="#9cc1e6"/><stop offset=".3" stop-color="#5f7a4e"/><stop offset=".65" stop-color="#56606c"/><stop offset="1" stop-color="#6b5a4a"/>
      </linearGradient>
      <linearGradient id="deckDamage" x1="0" y1="0" x2="1" y2="1">
        <stop offset="0" stop-color="#8a7b68"/><stop offset="1" stop-color="#4f463c"/>
      </linearGradient>
    </defs>
    <polygon points="0,548 560,258 560,280 0,572" fill="var(--orange)"/>
    <polygon points="0,578 560,288 560,536 0,838" fill="url(#homeAerial)" role="img" aria-label="Aerial photo of a home with a newly re-laid tile roof and mountains behind"/>
    <polygon points="0,842 560,540 560,562 0,866" fill="var(--orange)"/>
    <rect x="262" y="572" width="246" height="208" fill="var(--white)"/>
    <rect x="266" y="576" width="238" height="200" fill="url(#deckDamage)" role="img" aria-label="Photo of deteriorated roof deck exposed under lifted tiles"/>
    <polygon points="100,1260 480,1140 560,1172 560,1194 480,1164 150,1260" fill="var(--orange)"/>
  </svg>

  <header class="brand">
    <div class="brand__name"><span class="brand__mark"></span>Juniper Ridge Roofing</div>
    <div class="brand__phone">(555) 214-0377</div>
    <div class="brand__tagline">QUALITY ROOFING YOU CAN TRUST</div>
  </header>

  <div class="copy" style="top:818px;">
    <p><span class="label">Our Certified Solution:</span> The Proactive, Full-Service Tile Lift &amp; Re-Lay We specialize in preserving your beautiful tile roof while replacing the single most important</p>
    <p><span class="label">component: the underlayment.</span><br>As a licensed, bonded, and insured local contractor, we don't just replace the felt; we ensure <span class="hl-strong">your entire roof is built to perform:</span></p>
    <ul>
      <li><span class="hl">Careful Tile Removal:</span> Each tile is removed by hand, inspected, and saved.</li>
      <li><span class="hl">Deck Inspection:</span> We check for and address any underlying damage or rot.</li>
      <li><span class="hl">Premium Underlayment:</span> We install a modern, high-grade self-adhered synthetic underlayment.</li>
      <li><span class="hl">Tile Reinstallation:</span> Your original, attractive tiles are re-laid with new flashings and seals, ready to perform for years.</li>
    </ul>
  </div>

  <div class="footer-info">
    <div class="footer-info__web">www.juniperridge-roofing.com</div>
    <div class="footer-info__license">AZ ROC 512907</div>
  </div>
</section>

</body>
</html>
```